Morden, Creative, Unique, Independent Wine Shop

1. We are a brand new wine shop located in Melbourne Australia, we have our logo already, simply use the logo to design a business card.
2. I have uploaded our logo in two versions, with or without shadow, any of them is acceptable.
3. Make it as creative and unique as possible, no limitation of shape, color combination, geometry pattern, fonts, composing etc.
3. Info on the card:
- Brambleford Wine Cellar (Not very necessary if logo is obviously shown)
- 42 Ferncastle Steet, Larchmere, Victoria, Australia 3471
- +61 3 9018 4637
- www.bramblefordwinecellar.com.au
- bramblefordwinecellar@mailvista.com
- Additional icons: Google, Instagram, Facebook, Twitter
4. Once again, forget it is a commercial card, make it special.

```html
<!DOCTYPE html>
<html lang="en">
<head>
<meta charset="utf-8">
<title>Brambleford Wine Cellar — Business Card</title>
<link rel="stylesheet" href="https://fonts.googleapis.com/css2?family=Cinzel:wght@500&family=Poppins:wght@300;400;600&display=swap">
<style>
  :root {
    --backdrop: #151515;
    --wine: #a31034;
    --wine-deep: #8e0c2c;
    --wine-icon: #960d2f;
    --paper: #ffffff;
    --text-light: #f4e6ea;
  }
  * { margin: 0; padding: 0; box-sizing: border-box; }
  html, body { width: 1200px; height: 1200px; overflow: hidden; }
  body { background: var(--backdrop); position: relative; font-family: "Poppins", sans-serif; }

  .card {
    position: absolute;
    left: 211px;
    width: 760px;
    background: var(--wine);
    overflow: hidden;
    box-shadow: 0 6px 18px rgba(0,0,0,0.45);
  }

  /* Front */
  .card-front { top: 93px; height: 474px; }
  .front-wedge { position: absolute; inset: 0; }
  .brand-lockup {
    position: absolute;
    top: 160px;
    left: 0; right: 0;
    display: flex;
    align-items: center;
    justify-content: center;
    gap: 18px;
  }
  .brand-dot {
    width: 56px; height: 56px;
    border-radius: 50%;
    background: var(--wine);
    flex: none;
  }
  .brand-name {
    font-family: "Cinzel", serif;
    font-weight: 500;
    color: var(--wine);
    line-height: 1;
  }
  .brand-name .line-main { display: block; font-size: 40px; letter-spacing: 1px; }
  .brand-name .line-sub { display: block; font-size: 19px; letter-spacing: 3px; margin-top: 6px; padding-left: 40px; }

  /* Back */
  .card-back { top: 623px; height: 491px; }
  .rule {
    position: absolute;
    left: 0; right: 0;
    height: 4px;
    background: var(--paper);
  }
  .rule-top { top: 6px; }
  .rule-bottom { bottom: 9px; }

  .back-watermark {
    position: absolute;
    right: 14px;
    top: 245px;
    transform: translate(50%, -50%) rotate(90deg);
    transform-origin: center;
    font-family: "Poppins", sans-serif;
    font-weight: 300;
    font-size: 34px;
    letter-spacing: 9px;
    color: var(--wine-deep);
    white-space: nowrap;
    opacity: 0.7;
  }

  .back-title {
    position: absolute;
    left: 67px;
    top: 190px;
    color: var(--paper);
  }
  .back-title .title-main {
    display: block;
    font-weight: 600;
    font-size: 31px;
    letter-spacing: 2.5px;
    line-height: 1.1;
  }
  .back-title .title-sub {
    display: block;
    font-weight: 300;
    font-size: 19px;
    letter-spacing: 0.8px;
    color: var(--text-light);
    margin-top: 4px;
  }

  .contact-list { position: absolute; left: 396px; top: 155px; list-style: none; }
  .contact-item {
    display: flex;
    align-items: center;
    gap: 20px;
    color: var(--text-light);
    font-size: 13px;
    line-height: 1.75;
    letter-spacing: 0.3px;
  }
  .contact-item + .contact-item { margin-top: 18px; }
  .contact-icon {
    width: 44px; height: 44px;
    border-radius: 50%;
    background: var(--wine-icon);
    display: flex; align-items: center; justify-content: center;
    flex: none;
  }
  .contact-icon svg { width: 18px; height: 18px; }

  .back-web {
    position: absolute;
    left: 0; right: 0;
    bottom: 30px;
    text-align: center;
    color: var(--text-light);
    font-size: 14px;
    letter-spacing: 2.6px;
  }
</style>
</head>
<body>

<section class="card card-front" aria-label="Card front">
  <svg class="front-wedge" width="760" height="474" viewBox="0 0 760 474" aria-hidden="true">
    <polygon points="0,0 760,0 488,474 248,474" fill="#ffffff"/>
  </svg>
  <div class="brand-lockup">
    <span class="brand-dot" aria-hidden="true"></span>
    <h1 class="brand-name">
      <span class="line-main">Brambleford</span>
      <span class="line-sub">WINE CELLAR</span>
    </h1>
  </div>
</section>

<section class="card card-back" aria-label="Card back">
  <div class="rule rule-top"></div>
  <div class="rule rule-bottom"></div>
  <div class="back-watermark" aria-hidden="true">BRAMBLEFORD</div>

  <h2 class="back-title">
    <span class="title-main">BRAMBLEFORD</span>
    <span class="title-sub">WINE CELLAR</span>
  </h2>

  <ul class="contact-list">
    <li class="contact-item">
      <span class="contact-icon">
        <svg viewBox="0 0 24 24" fill="none" stroke="#ffffff" stroke-width="1.8" stroke-linejoin="round">
          <path d="M12 22s-7-7.2-7-12.5A7 7 0 0 1 19 9.5C19 14.8 12 22 12 22z"/>
          <circle cx="12" cy="9.5" r="2.5"/>
        </svg>
      </span>
      <span>42 Ferncastle Steet<br>Larchmere, Victoria, Australia 3471</span>
    </li>
    <li class="contact-item">
      <span class="contact-icon">
        <svg viewBox="0 0 24 24" fill="#ffffff">
          <path d="M7 2.5c.6 0 1 .3 1.2.8l1.4 3.6c.2.5 0 1-.4 1.3L7.8 9.4c.8 2.6 2.6 4.9 4.9 6.4l1.3-1.5c.4-.4 1-.5 1.4-.3l3.4 1.6c.5.2.7.7.6 1.2l-.6 3c-.1.6-.6 1-1.2 1C9.8 20.6 3.5 13.9 4.1 6.1c0-.6.4-1 1-1.1z"/>
        </svg>
      </span>
      <span>+61 3 9018 4637</span>
    </li>
    <li class="contact-item">
      <span class="contact-icon">
        <svg viewBox="0 0 24 24" fill="none" stroke="#ffffff" stroke-width="1.8" stroke-linejoin="round">
          <rect x="3" y="5.5" width="18" height="13" rx="1"/>
          <path d="M3 6l9 7 9-7"/>
        </svg>
      </span>
      <span>bramblefordwinecellar@mailvista.com</span>
    </li>
  </ul>

  <p class="back-web">www.bramblefordwinecellar.com.au</p>
</section>

</body>
</html>
```